Natural Skincare brand needs new labels!

We are a natural and organic skin care brand based in the united states. We are looking for unique product label designs that will help our brand stand out. We want the labels to look elegant and natural, but also incorporate some color. We want a design aspect like a line drawing on the labels, see examples. Please refer to our website to see our current labels and to get more of a feel of who we are. Our logo is included. We are looking for 5 labels for 5 different Products.
1. Body butter: 1.5"x9" rectangle wrap around 12oz jar with black lid
2. Eczema Salve: 1.5" circle silver metal tin
3. Glow Serum: 1.5"x3" rectangle Blue Dropper Bottle with black top
4. Mineral Mist: 1.5"x3" clear glass sprayer bottle (want clear label)
website: www.velmirabotanics.com
Instagram: @velmirabotanics

```html
<!DOCTYPE html>
<html lang="en">
<head>
<meta charset="utf-8">
<title>Velmira Labels</title>
<link href="https://fonts.googleapis.com/css2?family=Oswald:wght@400;500;700&family=Anton&family=Montserrat:wght@400&display=swap" rel="stylesheet">
<style>
  :root{
    --page:#ececec;
    --orange:#ff5a00;
    --orange-deep:#c0440a;
    --white:#ffffff;
    --purple:#8a1fb8;
    --purple-bg:#a62cc8;
    --purple-dark:#5b1487;
    --purple-mid:#7a22b0;
    --purple-soft:#b46ad6;
  }
  *{box-sizing:border-box;margin:0;padding:0}
  html,body{width:714px;height:1200px;overflow:hidden;background:var(--page)}
  body{font-family:"Oswald",sans-serif;display:flex;flex-direction:column;align-items:center;justify-content:space-evenly;padding:20px 0}

  .label{width:620px;height:310px;display:grid;grid-template-columns:150px 1fr 150px;padding:20px 16px;gap:10px;position:relative}
  .label--serum{background:var(--orange);color:var(--white)}
  .label--mist-clear{background:var(--white);color:var(--purple);grid-template-columns:140px 44px 1fr 140px}
  .label--mist-purple{background:var(--purple-bg);color:var(--white)}

  .copy{font-size:13.5px;line-height:1.3;text-align:center;font-weight:400}
  .copy p+p{margin-top:16px}
  .side{display:flex;flex-direction:column;justify-content:space-between;align-items:center;padding-top:4px}

  .front{display:flex;flex-direction:column;align-items:center;text-align:center;min-width:0}
  .brand{display:flex;align-items:center;gap:6px;font-weight:500;letter-spacing:1px;white-space:nowrap}
  .brand__dot{width:11px;height:11px;border-radius:50%;background:currentColor}
  .brand--main{font-size:34px;line-height:1}
  .brand--small{font-size:20px;padding-bottom:8px}
  .brand--muted{color:var(--purple-dark)}

  .art{flex:1;min-height:0;margin:8px 0 6px;border-radius:6px}
  .art--flower{width:140px;background:linear-gradient(180deg,var(--orange-deep),var(--orange))}
  .art--crystal{width:70px;background:linear-gradient(180deg,var(--purple-soft),var(--purple-mid))}
  .art--crystal-dark{width:130px;background:linear-gradient(180deg,var(--purple-mid),var(--purple-dark))}

  .title{font-family:"Anton",sans-serif;font-weight:400;font-size:34px;line-height:1.05;white-space:nowrap}
  .sub{font-size:15px;line-height:1.15;text-transform:uppercase;white-space:nowrap}
  .size{font-family:"Montserrat",sans-serif;font-size:22px;line-height:1.2;margin-top:4px}

  .balance{font-weight:700;font-size:30px;letter-spacing:9px;color:var(--purple);white-space:nowrap}
  .balance--vertical{writing-mode:vertical-rl;transform:rotate(180deg);align-self:center;justify-self:center}
  .balance--inline{color:var(--purple-dark);line-height:1.1;margin-top:2px}
</style>
</head>
<body>

  <section class="label label--serum">
    <div class="side copy">
      <div>
        <p>Get ready to glow. A golden serum that's perfect for brightening dull skin with the powerhouse herb, manjistha. The glycosides in manjistha improve complexion and lighten dark spots.</p>
        <p>Apply daily or as needed.</p>
      </div>
    </div>
    <div class="front">
      <div class="brand brand--main"><span class="brand__dot"></span>Velmira</div>
      <div class="art art--flower" role="img" aria-label="Line drawing of a safflower plant"></div>
      <h1 class="title">GLOW SERUM</h1>
      <p class="sub">Manjistha + Safflower<br>Glow + Even Skin Tone</p>
      <p class="size">1 oz.</p>
    </div>
    <div class="side copy">
      <p>Ingredients: safflower oil, sesame oil, manjistha powder, rose petals, turmeric, carrot seed oil, sandalwood essential oil, ylang ylang essential oil organic</p>
      <div class="brand brand--small"><span class="brand__dot"></span>Velmira</div>
    </div>
  </section>

  <section class="label label--mist-clear">
    <div class="side copy">
      <p>Minerals like tourmaline, red clay, Kaolin earth, and nano silver work together as a multipurpose, alkaline antioxidant solution that can reduce skin irritation and the appearance of inflammation.</p>
    </div>
    <div class="balance balance--vertical">BALANCE</div>
    <div class="front">
      <div class="brand brand--main"><span class="brand__dot"></span>Velmira</div>
      <div class="art art--crystal" role="img" aria-label="Illustration of an amethyst crystal cluster"></div>
      <h1 class="title">MINERAL MIST</h1>
      <p class="sub">Amethyst + Rose Quartz</p>
      <p class="size">2 oz.</p>
    </div>
    <div class="side copy">
      <p>Cleanse, protect, and revitalize skin's barrier with an essential nutrient mist.</p>
      <div class="brand brand--small"><span class="brand__dot"></span>Velmira</div>
    </div>
  </section>

  <section class="label label--mist-purple">
    <div class="side copy">
      <p>Minerals like tourmaline, red clay, Kaolin earth, and nano silver work together as a multipurpose, alkaline antioxidant solution that can reduce skin irritation and the appearance of inflammation.</p>
    </div>
    <div class="front">
      <div class="brand brand--main"><span class="brand__dot"></span>Velmira</div>
      <div class="art art--crystal-dark" role="img" aria-label="Illustration of a large amethyst crystal cluster"></div>
      <h1 class="title">MINERAL MIST</h1>
      <p class="sub">Amethyst + Rose Quartz</p>
      <p class="balance balance--inline">BALANCE</p>
      <p class="size">2 oz.</p>
    </div>
    <div class="side copy">
      <p>Cleanse, protect, and revitalize skin's barrier with an essential nutrient mist.</p>
      <div class="brand brand--small brand--muted"><span class="brand__dot"></span>Velmira</div>
    </div>
  </section>

</body>
</html>
```